Security Consulting firm needs an ad design

We need a 3.375” x 4.875” ad design for our core services. The ad should include the company logo and the content from the first half of the attached sample JPG (Without the sentence under the title but including the description for the Plan - Design - Deploy - Manage and the titles ) as well as the following corporate information:
www.harborlanepartners.us
82 Morrow Ave. Suite 615, Brookhaven Falls, NJ 07519
PHONE 888-416-2057 / EMAIL info@harborlanepartners.us
The design should incorporate the same blue color that is in our logo and the font Raleway. Also - please use the same icons that are in the sample JPG - they can also be extracted from the attached indesign file.
The ad is to be publish in print and digital issue.
Please provide with all source files as well as a hi-res PDF using press quality or similar PDF settings.
- Raleway

```html
<!DOCTYPE html>
<html lang="en">
<head>
<meta charset="utf-8">
<title>Harborlane Partners – Creating Secure Environments</title>
<link href="https://fonts.googleapis.com/css2?family=Raleway:wght@400;500;600;700;800&display=swap" rel="stylesheet">
<style>
  :root {
    --brand-blue: #2f6db3;
    --footer-blue: #3471b6;
    --ink: #3a3f45;
    --muted: #5b6168;
    --rule: #c9ced4;
    --paper: #ffffff;
    --icon-ring: #e3e8ee;
  }
  * { margin: 0; padding: 0; box-sizing: border-box; }
  html, body { width: 824px; height: 1200px; overflow: hidden; background: var(--paper); }
  body { font-family: "Raleway", Arial, sans-serif; color: var(--ink); }

  .ad { position: relative; width: 824px; height: 1200px; background: var(--paper); overflow: hidden; }

  .hero {
    position: absolute; left: 0; top: 0; width: 824px; height: 595px;
    background: linear-gradient(160deg, #eef1f4 0%, #dfe4ea 35%, #8fa3b8 60%, #3d5874 85%, #2b3e55 100%);
  }

  .brand {
    position: absolute; left: 40px; top: 40px;
    display: flex; align-items: center; gap: 14px;
  }
  .brand-mark { width: 44px; height: 44px; border-radius: 50%; background: var(--brand-blue); }
  .brand-name { font-size: 38px; font-weight: 700; color: var(--brand-blue); letter-spacing: 0.5px; }

  .headline {
    position: absolute; left: 68px; top: 628px;
    font-size: 60px; line-height: 1.1; font-weight: 400; color: var(--ink);
    letter-spacing: 0.5px; text-transform: uppercase;
  }
  .headline strong { font-weight: 800; color: var(--brand-blue); }

  .divider { position: absolute; left: 68px; top: 778px; width: 660px; height: 3px; background: var(--rule); }
  .divider::before { content: ""; position: absolute; left: 0; top: -2px; width: 110px; height: 7px; background: var(--brand-blue); }

  .services {
    position: absolute; left: 64px; top: 835px; width: 700px;
    display: grid; grid-template-columns: 350px 350px; row-gap: 38px;
  }
  .service { display: flex; gap: 18px; align-items: flex-start; }
  .service-icon {
    flex: none; width: 72px; height: 72px; border-radius: 50%;
    background: var(--paper); border: 2px solid var(--icon-ring);
    box-shadow: 0 3px 8px rgba(0,0,0,0.12);
    display: flex; align-items: center; justify-content: center;
  }
  .service-title { font-size: 30px; font-weight: 800; color: var(--brand-blue); text-transform: uppercase; line-height: 1.1; }
  .service-text { font-size: 20px; font-weight: 500; color: var(--muted); line-height: 1.25; margin-top: 4px; }

  .footer {
    position: absolute; left: 0; top: 1092px; width: 824px; height: 108px;
    background: var(--footer-blue); color: #fff;
    display: flex; align-items: center; justify-content: space-between; padding: 0 34px;
  }
  .contact { display: flex; flex-direction: column; gap: 6px; }
  .contact-line { display: flex; align-items: center; gap: 8px; white-space: nowrap; }
  .phone { font-size: 27px; font-weight: 800; }
  .email { font-size: 14px; font-weight: 500; }
  .address { display: flex; align-items: center; gap: 8px; font-size: 14px; font-weight: 500; line-height: 1.4; white-space: nowrap; }
  .website { font-size: 21px; font-weight: 700; letter-spacing: 0.2px; white-space: nowrap; }
</style>
</head>
<body>
<main class="ad">
  <div class="hero" role="img" aria-label="Photo of a security operator at a desk watching a wall of surveillance monitors"></div>

  <div class="brand">
    <span class="brand-mark"></span>
    <span class="brand-name">Harborlane Partners</span>
  </div>

  <h1 class="headline">Creating <strong>Secure</strong><br><strong>Environments</strong></h1>
  <div class="divider"></div>

  <section class="services">
    <div class="service">
      <div class="service-icon">
        <svg width="34" height="38" viewBox="0 0 34 38" fill="none" stroke="#2f6db3" stroke-width="2.5" stroke-linejoin="round" stroke-linecap="round">
          <rect x="3" y="5" width="28" height="31" rx="2"/>
          <rect x="11" y="2" width="12" height="6" rx="1"/>
          <path d="M8 16l2 2 4-4M8 26l2 2 4-4M18 16h8M18 27h8"/>
        </svg>
      </div>
      <div>
        <h2 class="service-title">Plan</h2>
        <p class="service-text">Security assessment and planning services</p>
      </div>
    </div>
    <div class="service">
      <div class="service-icon">
        <svg width="38" height="38" viewBox="0 0 38 38" fill="none" stroke="#2f6db3" stroke-width="2.5" stroke-linecap="round" stroke-linejoin="round">
          <circle cx="15" cy="15" r="5"/>
          <path d="M15 3v4M15 23v4M3 15h4M23 15h4M6.5 6.5l3 3M20.5 20.5l3 3M6.5 23.5l3-3M20.5 9.5l3-3"/>
          <path d="M24 24l10 10"/>
        </svg>
      </div>
      <div>
        <h2 class="service-title">Design</h2>
        <p class="service-text">Security design and engineering</p>
      </div>
    </div>
    <div class="service">
      <div class="service-icon">
        <svg width="36" height="36" viewBox="0 0 36 36" fill="#2f6db3">
          <path d="M33 3c-9 0-16 5-20 12l-6 1-4 5 7 1 5 5 1 7 5-4 1-6c7-4 12-11 11-21zM24 9a3 3 0 1 1 0 6 3 3 0 0 1 0-6z"/>
          <path d="M8 26c-3 1-4 4-5 7 3-1 6-2 7-5z"/>
        </svg>
      </div>
      <div>
        <h2 class="service-title">Deploy</h2>
        <p class="service-text">Procurement and Project Management Services</p>
      </div>
    </div>
    <div class="service">
      <div class="service-icon">
        <svg width="38" height="36" viewBox="0 0 38 36" fill="#2f6db3">
          <circle cx="19" cy="7" r="5"/>
          <path d="M12 20a7 7 0 0 1 14 0z"/>
          <circle cx="7" cy="20" r="4"/>
          <path d="M1 32a6 6 0 0 1 12 0z"/>
          <circle cx="31" cy="20" r="4"/>
          <path d="M25 32a6 6 0 0 1 12 0z"/>
        </svg>
      </div>
      <div>
        <h2 class="service-title">Manage</h2>
        <p class="service-text">Comprehensive security program management</p>
      </div>
    </div>
  </section>

  <footer class="footer">
    <div class="contact">
      <div class="contact-line phone">
        <svg width="22" height="22" viewBox="0 0 24 24" fill="#fff"><path d="M6.6 10.8a15.5 15.5 0 0 0 6.6 6.6l2.2-2.2c.3-.3.7-.4 1-.2 1.1.4 2.3.6 3.6.6.6 0 1 .4 1 1V20c0 .6-.4 1-1 1A17 17 0 0 1 3 4c0-.6.4-1 1-1h3.5c.6 0 1 .4 1 1 0 1.3.2 2.5.6 3.6.1.3 0 .7-.2 1z"/></svg>
        888-416-2057
      </div>
      <div class="contact-line email">
        <svg width="16" height="12" viewBox="0 0 16 12" fill="#fff"><path d="M0 1l8 5 8-5V0H0zM0 3v9h16V3L8 8z"/></svg>
        info@harborlanepartners.us
      </div>
    </div>
    <div class="address">
      <svg width="16" height="22" viewBox="0 0 16 22" fill="#fff"><path d="M8 0a8 8 0 0 0-8 8c0 6 8 14 8 14s8-8 8-14a8 8 0 0 0-8-8zm0 11a3 3 0 1 1 0-6 3 3 0 0 1 0 6z"/></svg>
      <span>82 Morrow Ave. Suite 615,<br>Brookhaven Falls, NJ 07519</span>
    </div>
    <div class="website">www.harborlanepartners.us</div>
  </footer>
</main>
</body>
</html>
```